Global Expert Network Firm needs business card design

We need business card design for a new company based in Seoul, South Korea called 'Corwell Insight Partners'. We recruit industry experts covering all countries and connect our client and recruited expert by phone, face-to-face meetings and etc. We are a global expert network firm that is focused on delivering high-quality experts to our clients throughout the world. Our clients include multinational corporations, global consulting firms, private equity firms, venture capital firms, asset management companies.
We have made new logo and please find attachment.(Please use new logo)
Target Market(s)
Global Consulting Firms, Investment Firms, Private Equity Firms, Venture Capital Firms.
Industry/Entity Type
Recruitment
Contact Information for Business Card
We need two Languages (English and Korean Version).
The front is Korean and the back is English version.
[The back] [English]
Company Name: Corwell Insight Partners, Inc.
CEO Name: Daniel Park
Address: #507, Hanbit Bldg, 82 Maebongsan-ro, Dobong-gu, Seoul, 01327, Korea
Tel. +82 2 718 4052
Fax. +82 2 864 1097
Mobile. +82 10 7264 8815
Email: daniel@corwellip.com
Web: www.corwellip.com
[The front] [Korean] => Described in same order as English version.
회사명: 코웰인사이트파트너스(주)
대표이사: 박도현
주소: 서울시 도봉구 매봉산로 82 한빛빌딩 507호
Tel. 02 718 4052
Fax. 02 864 1097
Mobile. 010 7264 8815
Web: www.corwellip.com
Look and feel
Each slider illustrates characteristics of the customer's brand and the style your logo design should communicate.

```html
<!DOCTYPE html>
<html lang="ko">
<head>
<meta charset="utf-8">
<title>Corwell Insight Partners — Business Card</title>
<link rel="stylesheet" href="https://fonts.googleapis.com/css2?family=Cormorant+Garamond:wght@500&family=Lato:wght@400&family=Noto+Sans+KR:wght@400&display=swap">
<style>
  :root {
    --navy: #141a3f;
    --paper: #ffffff;
    --backdrop: #e6e6e8;
    --ink: #141a3f;
    --ink-light: #f2f2f6;
  }
  * { box-sizing: border-box; margin: 0; padding: 0; }
  html, body { width: 1200px; height: 727px; overflow: hidden; }
  body {
    background: var(--backdrop);
    display: flex; align-items: center; justify-content: center; gap: 50px;
    font-family: "Lato", sans-serif;
  }
  .card {
    position: relative;
    width: 540px; height: 330px;
    border-radius: 30px;
    box-shadow: 0 2px 10px rgba(0,0,0,.12);
  }
  .card--front { background: var(--paper); color: var(--ink); }
  .card--back { background: var(--navy); color: var(--ink-light); }

  /* company name placeholder: plain text in the body font with one plain square */
  .brand {
    position: absolute;
    display: flex; align-items: center; gap: 10px;
    padding-bottom: 12px;
    border-bottom: 1px solid currentColor;
  }
  .brand__mark { flex: none; background: currentColor; }
  .brand__name { font-family: "Lato", sans-serif; font-weight: 400; white-space: nowrap; }
  .card--front .brand { left: 150px; top: 50px; }
  .card--front .brand__mark { width: 14px; height: 14px; }
  .card--front .brand__name { font-size: 22px; }
  .card--back .brand { left: 300px; top: 40px; }
  .card--back .brand__mark { width: 11px; height: 11px; }
  .card--back .brand__name { font-size: 17px; }

  .address { position: absolute; display: flex; gap: 8px; align-items: flex-start; }
  .card--front .address {
    left: 40px; top: 150px;
    font-family: "Noto Sans KR", sans-serif; font-size: 17px; line-height: 1.4;
  }
  .card--back .address { left: 36px; top: 40px; font-size: 10px; line-height: 1.6; width: 240px; }

  .contacts { position: absolute; list-style: none; text-align: right; }
  .contacts li { display: flex; align-items: center; justify-content: flex-end; gap: 8px; white-space: nowrap; }
  .card--front .contacts { right: 34px; bottom: 30px; }
  .card--front .contacts li { font-size: 15px; height: 26px; }
  .card--back .contacts { right: 280px; bottom: 26px; }
  .card--back .contacts li { font-size: 11px; height: 21px; }

  .icon { flex: none; }
  .card--front .icon { width: 20px; height: 20px; }
  .card--back .icon { width: 16px; height: 16px; }

  .person { position: absolute; right: 40px; top: 170px; text-align: right; }
  .person__name { font-family: "Cormorant Garamond", serif; font-size: 28px; font-weight: 500; }
  .person__title { font-size: 10px; letter-spacing: 1px; margin-top: 2px; }
</style>
</head>
<body>
<svg width="0" height="0" style="position:absolute" aria-hidden="true">
  <defs>
    <symbol id="ic-pin" viewBox="0 0 20 20"><circle cx="10" cy="10" r="10" fill="currentColor"/><path d="M10 4.5a3.5 3.5 0 0 0-3.5 3.5c0 2.6 3.5 7 3.5 7s3.5-4.4 3.5-7A3.5 3.5 0 0 0 10 4.5zm0 4.8a1.3 1.3 0 1 1 0-2.6 1.3 1.3 0 0 1 0 2.6z" fill="var(--bg)"/></symbol>
    <symbol id="ic-phone" viewBox="0 0 20 20"><circle cx="10" cy="10" r="10" fill="currentColor"/><path d="M7 5l2 2.2-1 1.3c.7 1.5 1.9 2.7 3.4 3.4l1.3-1L15 13l-1 1.8c-4.6-.3-8.4-4.1-8.8-8.8z" fill="var(--bg)"/></symbol>
    <symbol id="ic-fax" viewBox="0 0 20 20"><circle cx="10" cy="10" r="10" fill="currentColor"/><rect x="5" y="8" width="10" height="6" rx="1" fill="var(--bg)"/><rect x="7" y="5" width="6" height="3" fill="var(--bg)"/></symbol>
    <symbol id="ic-mobile" viewBox="0 0 20 20"><circle cx="10" cy="10" r="10" fill="currentColor"/><rect x="7" y="4.5" width="6" height="11" rx="1" fill="none" stroke="var(--bg)" stroke-width="1.4"/></symbol>
    <symbol id="ic-mail" viewBox="0 0 20 20"><circle cx="10" cy="10" r="10" fill="currentColor"/><rect x="5" y="6.5" width="10" height="7" fill="var(--bg)"/><path d="M5 6.5l5 4 5-4" fill="none" stroke="currentColor" stroke-width="1"/></symbol>
    <symbol id="ic-web" viewBox="0 0 20 20"><circle cx="10" cy="10" r="10" fill="currentColor"/><g fill="none" stroke="var(--bg)" stroke-width="1"><circle cx="10" cy="10" r="5"/><ellipse cx="10" cy="10" rx="2.2" ry="5"/><path d="M5 10h10M6 7.5h8M6 12.5h8"/></g></symbol>
  </defs>
</svg>

<section class="card card--front" style="--bg: var(--paper)">
  <div class="brand">
    <span class="brand__mark"></span>
    <span class="brand__name">Corwell Insight Partners</span>
  </div>
  <div class="address">
    <svg class="icon" style="color:var(--navy)"><use href="#ic-pin"/></svg>
    <p>서울시 도봉구 매봉산로 82<br>한빛빌딩 507호</p>
  </div>
  <ul class="contacts" style="color:var(--navy)">
    <li>+82 2 718 4052 <svg class="icon"><use href="#ic-phone"/></svg></li>
    <li>+82 2 864 1097 <svg class="icon"><use href="#ic-fax"/></svg></li>
    <li>+82 10 7264 8815 <svg class="icon"><use href="#ic-mobile"/></svg></li>
    <li>daniel@corwellip.com <svg class="icon"><use href="#ic-mail"/></svg></li>
    <li>www.corwellip.com <svg class="icon"><use href="#ic-web"/></svg></li>
  </ul>
</section>

<section class="card card--back" style="--bg: var(--navy)">
  <div class="brand">
    <span class="brand__mark"></span>
    <span class="brand__name">Corwell Insight Partners</span>
  </div>
  <div class="address">
    <svg class="icon" style="color:var(--ink-light)"><use href="#ic-pin"/></svg>
    <p>#507, Hanbit Bldg, 82 Maebongsan-ro,<br>Dobong-gu, Seoul, 01327, Korea</p>
  </div>
  <div class="person">
    <div class="person__name">Daniel Park</div>
    <div class="person__title">CEO</div>
  </div>
  <ul class="contacts" style="color:var(--ink-light)">
    <li>+82 2 718 4052 <svg class="icon"><use href="#ic-phone"/></svg></li>
    <li>+82 2 864 1097 <svg class="icon"><use href="#ic-fax"/></svg></li>
    <li>+82 10 7264 8815 <svg class="icon"><use href="#ic-mobile"/></svg></li>
    <li>daniel@corwellip.com <svg class="icon"><use href="#ic-mail"/></svg></li>
    <li>www.corwellip.com <svg class="icon"><use href="#ic-web"/></svg></li>
  </ul>
</section>
</body>
</html>
```